Accounting services

Looking for a Business card & Logo design

company name - QUELM ACCOUNTING & TAXATION SOLUTIONS

name - Corwin Belto

position - Accountant / Business Consultant

email - "undecided"

Tel : (868) 512-0000 / (868) 287-0000

**PUT THESE TO THE BACK**
Accounting - VAT * INCOME/CORP TAX * RETURNS

REGISTRATION - VAT * NIS * Company Registration/Business Plan

```html
<!DOCTYPE html>
<html lang="en">
<head>
<meta charset="utf-8">
<title>QUELM Accounting &amp; Taxation Solutions – Business Card</title>
<link href="https://fonts.googleapis.com/css2?family=Open+Sans:wght@400;600;700&family=Roboto+Condensed:wght@400;700&display=swap" rel="stylesheet">
<style>
  :root {
    --brand-blue: #35a8e0;
    --brand-grey: #6f6f6f;
    --ink: #1e1e1e;
    --paper: #ffffff;
    --backdrop: #eceae6;
    --divider: rgba(255,255,255,0.55);
  }
  * { box-sizing: border-box; margin: 0; padding: 0; }
  html, body { width: 1200px; height: 970px; overflow: hidden; }
  body {
    background: var(--backdrop);
    display: flex;
    align-items: center;
    justify-content: center;
    gap: 100px;
  }
  .card {
    width: 400px;
    height: 700px;
    position: relative;
    box-shadow: 0 6px 18px rgba(0,0,0,0.18);
  }

  /* Back side */
  .card--back {
    background: var(--brand-blue);
    color: var(--paper);
    font-family: "Roboto Condensed", Arial, sans-serif;
    text-align: center;
  }
  .back-mark {
    position: absolute;
    top: 150px;
    left: 0; right: 0;
    display: flex;
    align-items: center;
    justify-content: center;
    gap: 14px;
    font-family: "Open Sans", Arial, sans-serif;
    font-weight: 700;
    font-size: 54px;
    letter-spacing: 3px;
    color: var(--paper);
  }
  .back-mark__dot {
    width: 26px; height: 26px;
    border-radius: 50%;
    background: var(--paper);
  }
  .services {
    position: absolute;
    top: 440px;
    left: 0; right: 0;
    padding: 0 22px;
  }
  .service__title {
    font-weight: 700;
    font-size: 26px;
    letter-spacing: 0.5px;
  }
  .service__items {
    font-size: 16px;
    margin-top: 4px;
    letter-spacing: 0.3px;
  }
  .service__divider {
    width: 230px;
    height: 1px;
    background: var(--divider);
    margin: 12px auto 10px;
  }

  /* Front side */
  .card--front {
    background: var(--paper);
    font-family: "Open Sans", Arial, sans-serif;
  }
  .front-mark {
    position: absolute;
    top: 82px;
    left: 40px;
    display: flex;
    align-items: flex-start;
    gap: 14px;
    color: var(--brand-blue);
    font-weight: 700;
  }
  .front-mark__square {
    width: 48px; height: 48px;
    background: var(--brand-blue);
    flex: none;
    margin-top: 4px;
  }
  .front-mark__name { font-size: 46px; line-height: 1; letter-spacing: 2px; }
  .front-mark__tagline { font-size: 17px; line-height: 1.2; margin-top: 6px; letter-spacing: 0.5px; }

  .person {
    position: absolute;
    top: 360px;
    right: 34px;
    text-align: right;
  }
  .person__name { font-size: 28px; font-weight: 400; letter-spacing: -0.3px; }
  .person__first { color: var(--brand-blue); }
  .person__last { color: var(--brand-grey); }
  .person__role { font-size: 15px; font-weight: 600; color: var(--ink); margin-top: 2px; }

  .contacts {
    position: absolute;
    top: 470px;
    right: 34px;
    list-style: none;
    text-align: right;
  }
  .contact {
    display: flex;
    align-items: center;
    justify-content: flex-end;
    gap: 10px;
    font-size: 15px;
    color: var(--ink);
    margin-bottom: 14px;
  }
  .contact__icon { width: 16px; height: 16px; fill: var(--brand-blue); flex: none; }

  .front-band {
    position: absolute;
    left: 0; right: 0; bottom: 0;
    height: 34px;
    background: var(--brand-blue);
  }
</style>
</head>
<body>

  <section class="card card--back" aria-label="Card back">
    <div class="back-mark"><span class="back-mark__dot"></span>QUELM</div>
    <div class="services">
      <div class="service">
        <div class="service__title">ACCOUNTING</div>
        <div class="service__items">VAT &nbsp;|&nbsp; INCOME/CORP TAX &nbsp;|&nbsp; RETURNS</div>
      </div>
      <div class="service__divider"></div>
      <div class="service">
        <div class="service__title">REGISTRATION</div>
        <div class="service__items">VAT * NIS * Company Registration/Business Plan</div>
      </div>
    </div>
  </section>

  <section class="card card--front" aria-label="Card front">
    <div class="front-mark">
      <span class="front-mark__square"></span>
      <div>
        <div class="front-mark__name">QUELM</div>
        <div class="front-mark__tagline">ACCOUNTING &amp;<br>TAXATION SOLUTIONS</div>
      </div>
    </div>

    <div class="person">
      <div class="person__name"><span class="person__first">Corwin</span><span class="person__last">Belto</span></div>
      <div class="person__role">Accountant / Business Consultant</div>
    </div>

    <ul class="contacts">
      <li class="contact">(868) 512-0000
        <svg class="contact__icon" viewBox="0 0 16 16" aria-hidden="true"><path d="M3.2 1.5l2.3-.3 1.4 3.3-1.5 1.2a9 9 0 0 0 4.9 4.9l1.2-1.5 3.3 1.4-.3 2.3c-.1.6-.7 1.1-1.3 1.1A12.9 12.9 0 0 1 2.1 2.8c0-.6.5-1.2 1.1-1.3z"/></svg>
      </li>
      <li class="contact">(868) 287-0000
        <svg class="contact__icon" viewBox="0 0 16 16" aria-hidden="true"><path d="M4.5 0h7c.8 0 1.5.7 1.5 1.5v13c0 .8-.7 1.5-1.5 1.5h-7C3.7 16 3 15.3 3 14.5v-13C3 .7 3.7 0 4.5 0zM5 2v10h6V2H5zm3 11.2a.9.9 0 1 0 0 1.8.9.9 0 0 0 0-1.8z"/></svg>
      </li>
      <li class="contact">corwin.belto@quelmmail.com
        <svg class="contact__icon" viewBox="0 0 16 16" aria-hidden="true"><path d="M1 3.5h14v9H1v-9zm1.2 1L8 8.8l5.8-4.3H2.2zM2 11.5h12V5.7L8 10.1 2 5.7v5.8z"/></svg>
      </li>
    </ul>

    <div class="front-band"></div>
  </section>

</body>
</html>
```